NGO CHEMINS D'AURORE CAR COVERING

Hello, our NGO needs its covering.
Here are our wishes:
The vehicle is a white 2022 VORELLE KASTOR COMBI L2H1 with side windows at passengers side. The rear door is a double door.
Our NGO: we care about orphans and provide clear water to populations in Africa.
What must appear:
Our logo (hexa-color logo):
Brown: #8B5D3C (RGB: 139 93 60)
Green: #39B54A (RGB: 57 181 74)
Our motto: "An association that reflects you and unites us"
Phone number: 01 47 62 30 58
Add pixora, snapvelo and zumzee logo
As well as our site www.cheminsdaurore.com

Surprise us!!

No need of real photos on the project, just what is expressed on it. All scriptures must be in French.

```html
<!DOCTYPE html>
<html lang="fr">
<head>
<meta charset="utf-8">
<title>Chemins d'Aurore – habillage véhicule</title>
<link rel="stylesheet" href="https://fonts.googleapis.com/css2?family=Cinzel:wght@600&family=Playfair+Display:wght@500;600&display=swap">
<style>
  :root {
    --brand-brown: #8B5D3C;
    --brand-green: #39B54A;
    --wrap-green: #2f9e3f;
    --body-white: #f7f8f8;
    --glass: #2a2e32;
    --glass-frame: #1c1f22;
    --tyre: #1e1f21;
    --hub: #c9ccce;
    --backdrop: #e9eaea;
    --ink-white: #ffffff;
  }
  html, body {
    margin: 0;
    padding: 0;
    width: 1200px;
    height: 1113px;
    overflow: hidden;
    background: var(--backdrop);
  }
  .wrap-board { display: block; width: 1200px; height: 1113px; }
  .brand-title {
    font-family: "Cinzel", serif;
    font-weight: 600;
    font-size: 38px;
    fill: var(--brand-brown);
  }
  .contact-line {
    font-family: "Playfair Display", serif;
    font-weight: 600;
    font-size: 22px;
    fill: var(--brand-green);
  }
  .motto-line {
    font-family: "Playfair Display", serif;
    font-weight: 500;
    font-size: 21px;
    fill: var(--ink-white);
  }
  .partner-name {
    font-family: "Playfair Display", serif;
    font-weight: 500;
    font-size: 16px;
    fill: var(--ink-white);
  }
  .partner-dot { fill: var(--ink-white); }
  .logo-name {
    font-family: "Playfair Display", serif;
    font-weight: 600;
    font-size: 17px;
    fill: var(--brand-green);
  }
  .logo-ring { fill: none; stroke: var(--brand-brown); stroke-width: 7; }
  .van-body { fill: var(--body-white); stroke: #d5d8d9; stroke-width: 2; }
  .wrap-green { fill: var(--wrap-green); }
  .wrap-stripe { fill: none; stroke: var(--brand-brown); stroke-width: 14; }
  .glass { fill: var(--glass); stroke: var(--glass-frame); stroke-width: 6; }
  .glass-divider { stroke: var(--glass-frame); stroke-width: 8; }
  .sill { fill: #1f2224; }
  .sill-accent { fill: var(--brand-green); }
  .tyre { fill: var(--tyre); }
  .hub { fill: var(--hub); }
  .hub-centre { fill: #8d9194; }
</style>
</head>
<body>
<svg class="wrap-board" viewBox="0 0 1500 1391" xmlns="http://www.w3.org/2000/svg">
  <defs>
    <clipPath id="body-clip">
      <path d="M120,450 L118,345 Q125,305 175,290 L300,255 Q340,225 380,185 L460,120 Q490,100 540,98 L1340,95 Q1385,98 1388,150 L1388,480 Q1385,505 1360,505 L1240,505 A85 85 0 0 0 1075,505 L365,500 A85 85 0 0 0 200,490 L130,490 Q112,480 120,450 Z"/>
    </clipPath>
    <clipPath id="green-clip">
      <path d="M1240,90 L1400,90 L1400,530 L790,530 Q1000,440 1110,288 Q1180,185 1240,90 Z"/>
    </clipPath>
    <linearGradient id="people-tone" x1="0" y1="0" x2="1" y2="1">
      <stop offset="0" stop-color="#4fbf5c" stop-opacity="0.45"/>
      <stop offset="1" stop-color="#1f7a2e" stop-opacity="0.6"/>
    </linearGradient>

    <g id="van-side">
      <path class="van-body" d="M120,450 L118,345 Q125,305 175,290 L300,255 Q340,225 380,185 L460,120 Q490,100 540,98 L1340,95 Q1385,98 1388,150 L1388,480 Q1385,505 1360,505 L1240,505 A85 85 0 0 0 1075,505 L365,500 A85 85 0 0 0 200,490 L130,490 Q112,480 120,450 Z"/>
      <g clip-path="url(#body-clip)">
        <path class="wrap-green" d="M1240,90 L1400,90 L1400,530 L790,530 Q1000,440 1110,288 Q1180,185 1240,90 Z"/>
        <g clip-path="url(#green-clip)">
          <rect role="img" aria-label="Photo d'enfants et d'un bénévole souriants, fondue dans le vert" x="1000" y="250" width="400" height="280" fill="url(#people-tone)"/>
        </g>
        <path class="wrap-stripe" d="M1240,90 Q1178,188 1110,288 Q1000,440 795,485"/>
      </g>
      <path class="glass" d="M362,200 Q420,132 470,124 L592,125 L592,266 L372,290 Q350,286 352,252 Z"/>
      <rect class="glass" x="647" y="122" width="668" height="163" rx="30"/>
      <line class="glass-divider" x1="958" y1="124" x2="958" y2="283"/>
      <rect class="sill" x="380" y="482" width="680" height="34" rx="6"/>
      <rect class="sill-accent" x="380" y="516" width="680" height="9"/>
      <circle class="tyre" cx="280" cy="512" r="70"/>
      <circle class="hub" cx="280" cy="512" r="44"/>
      <circle class="hub-centre" cx="280" cy="512" r="12"/>
      <circle class="tyre" cx="1160" cy="522" r="72"/>
      <circle class="hub" cx="1160" cy="522" r="45"/>
      <circle class="hub-centre" cx="1160" cy="522" r="12"/>
    </g>
  </defs>

  <!-- Côté conducteur -->
  <use href="#van-side"/>
  <g class="brand-mark">
    <circle class="logo-ring" cx="460" cy="385" r="80"/>
    <text class="logo-name" x="460" y="391" text-anchor="middle">Chemins d'Aurore</text>
  </g>
  <text class="brand-title" x="823" y="347" text-anchor="middle">CHEMINS D'AURORE</text>
  <text class="contact-line" x="823" y="389" text-anchor="middle">cheminsdaurore.com</text>
  <text class="contact-line" x="823" y="416" text-anchor="middle">01 47 62 30 58</text>
  <text class="motto-line" x="1215" y="360" text-anchor="middle">Une association qui vous</text>
  <text class="motto-line" x="1215" y="388" text-anchor="middle">ressemble et nous rassemble</text>
  <g class="partner-row">
    <circle class="partner-dot" cx="1102" cy="424" r="5"/>
    <text class="partner-name" x="1111" y="429">pixora</text>
    <circle class="partner-dot" cx="1180" cy="424" r="5"/>
    <text class="partner-name" x="1189" y="429">snapvelo</text>
    <circle class="partner-dot" cx="1272" cy="424" r="5"/>
    <text class="partner-name" x="1281" y="429">zumzee</text>
  </g>

  <!-- Côté passager -->
  <use href="#van-side" transform="translate(1495,672) scale(-1,1)"/>
  <g class="brand-mark">
    <circle class="logo-ring" cx="1035" cy="1057" r="80"/>
    <text class="logo-name" x="1035" y="1063" text-anchor="middle">Chemins d'Aurore</text>
  </g>
  <text class="brand-title" x="672" y="1017" text-anchor="middle">CHEMINS D'AURORE</text>
  <text class="contact-line" x="672" y="1060" text-anchor="middle">cheminsdaurore.com</text>
  <text class="contact-line" x="672" y="1087" text-anchor="middle">01 47 62 30 58</text>
  <text class="motto-line" x="290" y="1032" text-anchor="middle">Une association qui vous</text>
  <text class="motto-line" x="290" y="1060" text-anchor="middle">ressemble et nous rassemble</text>
  <g class="partner-row">
    <circle class="partner-dot" cx="176" cy="1096" r="5"/>
    <text class="partner-name" x="185" y="1101">pixora</text>
    <circle class="partner-dot" cx="254" cy="1096" r="5"/>
    <text class="partner-name" x="263" y="1101">snapvelo</text>
    <circle class="partner-dot" cx="346" cy="1096" r="5"/>
    <text class="partner-name" x="355" y="1101">zumzee</text>
  </g>
</svg>
</body>
</html>
```